Billboard design - consider what a billboard is

Design a billboard using my logo - Billboard is 6m x 3m
A Billboard is advertising for my company that is on a big sign.

Has to be clean and easy to read, and ideally highlights that we are Residential and Commercial builders.

Keep it clean and easy to read

The contact number for the board is

022 583 7092
www.harbourframeworks.co.nz
info@harbourframeworks.co.nz

Doesnt have to have all contact details if it doesnt fit

Has to catch peoples attention to contact us if they need a builder

Can you please change the sign to be all white writing, with black background ?
Updates

Please consider what a billboard is...

The design needs to be suitable for a billboard..

Target Market(s)

people driving past

Industry/Entity Type

Construction

Logo Text

Wellington Builder, website email address, contact number

Colors
0054AA
0677BA
7BADD7
CADEEF
E8F1F8

Requirements
Must have
• Easy to read
Nice to have
• easy to read, can clearly see contact details

```html
<!DOCTYPE html>
<html lang="en">
<head>
<meta charset="utf-8">
<title>Harbour Frameworks Billboard</title>
<link rel="stylesheet" href="https://fonts.googleapis.com/css2?family=Montserrat:wght@300;600;700;800&display=swap">
<style>
  :root {
    --stage: #e4e4e4;
    --paper: #ffffff;
    --brand-blue: #5a8ac9;
    --brand-taupe: #746a69;
    --ink-light: #ffffff;
    --sky-top: #a6c7ee;
    --sky-low: #d3e3f2;
    --house-stone: #8a8580;
    --lawn: #5f9a2e;
    --tower-sky: #21467f;
    --tower-stone: #8e8470;
    --tower-glass: #3c4f52;
  }
  html, body {
    margin: 0;
    padding: 0;
    width: 1200px;
    height: 779px;
    overflow: hidden;
    background: var(--stage);
  }
  .billboard {
    position: absolute;
    left: 20px;
    top: 99px;
    width: 1160px;
    height: 580px;
    display: block;
    font-family: "Montserrat", Arial, sans-serif;
  }
  .board-base { fill: var(--paper); }
  .headline-band, .phone-plate { fill: var(--brand-blue); }
  .contact-band { fill: var(--brand-taupe); }
  .brand-mark { fill: var(--brand-taupe); }
  .brand-name { fill: var(--brand-blue); font-weight: 700; }
  .headline { fill: var(--ink-light); }
  .headline-light { font-weight: 300; }
  .headline-bold { font-weight: 800; }
  .phone-number { fill: var(--ink-light); font-weight: 700; }
  .phone-icon { fill: none; stroke: var(--ink-light); stroke-width: 7; stroke-linecap: round; stroke-linejoin: round; }
  .phone-handset { fill: var(--ink-light); }
  .website { fill: var(--ink-light); font-weight: 600; }
</style>
</head>
<body>
<svg class="billboard" viewBox="0 0 1880 940" preserveAspectRatio="none" xmlns="http://www.w3.org/2000/svg">
  <defs>
    <linearGradient id="homeTones" x1="0" y1="0" x2="0" y2="1">
      <stop offset="0" stop-color="var(--sky-top)"/>
      <stop offset="0.35" stop-color="var(--sky-low)"/>
      <stop offset="0.55" stop-color="var(--house-stone)"/>
      <stop offset="0.78" stop-color="var(--house-stone)"/>
      <stop offset="0.85" stop-color="var(--lawn)"/>
      <stop offset="1" stop-color="var(--lawn)"/>
    </linearGradient>
    <linearGradient id="towerTones" x1="0" y1="0" x2="1" y2="1">
      <stop offset="0" stop-color="var(--tower-sky)"/>
      <stop offset="0.35" stop-color="var(--tower-sky)"/>
      <stop offset="0.6" stop-color="var(--tower-stone)"/>
      <stop offset="1" stop-color="var(--tower-glass)"/>
    </linearGradient>
  </defs>

  <rect class="board-base" x="0" y="0" width="1880" height="940"/>

  <!-- Brand -->
  <g class="brand">
    <rect class="brand-mark" x="80" y="132" width="56" height="56"/>
    <text class="brand-name" x="158" y="185" font-size="60">Harbour Frameworks</text>
  </g>

  <!-- Headline -->
  <polygon class="headline-band" points="0,320 905,320 845,633 0,633"/>
  <g class="headline">
    <text class="headline-light" x="110" y="393" font-size="66" textLength="545" lengthAdjust="spacingAndGlyphs">YOUR TRUSTED</text>
    <text class="headline-bold" x="108" y="465" font-size="74" textLength="557" lengthAdjust="spacingAndGlyphs">RESIDENTIAL</text>
    <text class="headline-bold" x="112" y="520" font-size="52" textLength="548" lengthAdjust="spacingAndGlyphs">AND COMMERCIAL</text>
    <text class="headline-light" x="108" y="605" font-size="96" textLength="550" lengthAdjust="spacingAndGlyphs">BUILDERS</text>
  </g>

  <!-- Contact -->
  <polygon class="contact-band" points="0,750 886,750 850,940 0,940"/>
  <polygon class="phone-plate" points="168,703 818,703 792,818 150,818"/>
  <g class="phone-icon-group">
    <path class="phone-handset" d="M196,732 c6,-4 14,-4 18,2 l10,16 c3,5 1,11 -4,14 l-6,4 c4,12 12,22 24,28 l5,-5 c4,-4 11,-4 15,0 l13,13 c4,5 3,12 -2,16 l-8,6 c-10,7 -28,3 -44,-12 c-18,-17 -28,-40 -26,-56 c1,-7 3,-12 5,-14 z"/>
    <path class="phone-icon" d="M240,748 a16,16 0 0 1 16,16"/>
    <path class="phone-icon" d="M242,732 a32,32 0 0 1 30,30"/>
  </g>
  <text class="phone-number" x="272" y="790" font-size="76" textLength="475" lengthAdjust="spacingAndGlyphs">022 583 7092</text>
  <text class="website" x="52" y="888" font-size="42" textLength="760" lengthAdjust="spacingAndGlyphs">www.harbourframeworks.co.nz</text>

  <!-- Project imagery -->
  <polygon role="img" aria-label="Photo of a single-storey brick home with a grey shingle roof, front porch, garage and green lawn" fill="url(#homeTones)" points="1025,0 1518,0 1340,940 850,940"/>
  <polygon role="img" aria-label="Photo looking up at a tall commercial tower with stone cladding and glass windows against a deep blue sky" fill="url(#towerTones)" points="1560,0 1880,0 1880,940 1385,940"/>
</svg>
</body>
</html>
```